Asia based real estate financing firm needs and AWESOME design for a biz card -Harbor Lending Circle

Looking for a stylish, & corporate-looking business card for a real estate financing brokerage firm in Asia, offering global mortgage loans. I uploaded our current logos. We would like to add a splash of color (perhaps the house icon) or any other suggestions are open. For the winning designer, we have a lot of work! Thanks and best of luck!

Target Market(s)

Real estate investors globally. We want to look more like a BANK and NOT a real estate company. Please don't play up on a "house" design.

Industry/Entity Type

Banking

Contact Information for Business Card

Harbor Lending Circle
Peter Wilks
Co-Founder | Partner

14 Cassia Lane, Suite 310
Singapore 047219
www.hlc-example.asia
peterwilks@hlc-example.asia
+65 555-0142
WeChat: peterwilks

Colors

Designer to choose colors to be used in the design.

Requirements
Must have
• Must have the standard business requirements for a card; name, address, email, etc
• Can be horizontal or vertical.
Nice to have
• It would be great to see some sort of variation to the logo with a pop of color. Red is good as we're in Asia, however, other options work as well.
• Our tag line is - Boundless home loans. It doesn't have to be on the card but might be nice.
• I'd like to start seeing our tagline within the cards as well. - Boundless home loans.
• Also, please add our location. The location for this card is Singapore so perhaps it can be highlighted or emphasised in some way.
• Singapore | Hong Kong | Shanghai | Manila
• As we will soon open an office in Shanghai, having an option for both languages would be great.
Should not have
• I'm exceited and open to your creativity ... knock it out of the park!

```html
<!DOCTYPE html>
<html lang="en">
<head>
<meta charset="utf-8">
<title>Harbor Lending Circle — Business Card</title>
<link href="https://fonts.googleapis.com/css2?family=Open+Sans:wght@400;600;700&display=swap" rel="stylesheet">
<style>
  :root {
    --page-bg: #e4ded7;
    --frost-top: #f1f4f7;
    --frost-bottom: #f4eeee;
    --brand-red: #9a1b1f;
    --panel-red-dark: #6e070b;
    --panel-red: #8e1216;
    --panel-red-light: #a21d20;
    --band-red: #a5262a;
    --band-text: #f3dcd9;
    --name-beige: #dcc6a8;
    --title-text: #eadfd6;
    --address-text: #eee3dc;
    --contact-text: #c79a94;
    --icon-tone: #d4b0aa;
    --edge: rgba(255,255,255,0.7);
  }
  * { box-sizing: border-box; margin: 0; padding: 0; }
  html, body {
    width: 1200px; height: 1120px; overflow: hidden;
    background: var(--page-bg);
    font-family: "Open Sans", Arial, sans-serif;
  }
  .business-card {
    position: absolute; left: 99px; top: 274px;
    width: 1002px; height: 572px;
    display: flex;
    border: 1px solid var(--edge);
    box-shadow: 0 18px 40px rgba(60,30,20,0.18);
  }
  .brand-side {
    position: relative; width: 520px; height: 100%;
    background: linear-gradient(180deg, var(--frost-top) 0%, #f7f7f8 55%, var(--frost-bottom) 100%);
  }
  .brand-name {
    position: absolute; left: 0; right: 0; top: 232px;
    text-align: center;
    color: var(--brand-red);
    font-weight: 600; font-size: 40px; letter-spacing: 0.5px;
  }
  .tagline-band {
    position: absolute; left: 0; top: 469px;
    width: 520px; height: 47px;
    background: linear-gradient(90deg, var(--band-red), #b73a3c);
    display: flex; align-items: center; padding-left: 78px;
  }
  .tagline {
    color: var(--band-text); font-size: 23px; letter-spacing: 4px;
  }
  .contact-side {
    position: relative; flex: 1; height: 100%;
    background: linear-gradient(160deg, var(--panel-red-dark) 0%, var(--panel-red) 55%, var(--panel-red-light) 100%);
  }
  .pointer { position: absolute; left: 0; top: 100px; }
  .person-name {
    position: absolute; left: 53px; top: 92px;
    color: var(--name-beige); font-weight: 700; font-size: 34px;
  }
  .person-title {
    position: absolute; left: 53px; top: 136px;
    color: var(--title-text); font-size: 25px;
  }
  .address {
    position: absolute; left: 53px; top: 268px;
    color: var(--address-text); font-size: 25px; line-height: 33px;
    font-style: normal;
  }
  .contact-list {
    position: absolute; left: 53px; top: 360px; list-style: none;
  }
  .contact-item {
    display: flex; align-items: center; gap: 12px;
    height: 32.5px; color: var(--contact-text); font-size: 23px;
  }
  .contact-icon { width: 22px; height: 22px; flex: none; }
</style>
</head>
<body>
  <div class="business-card">
    <section class="brand-side">
      <div class="brand-name">Harbor Lending Circle</div>
      <div class="tagline-band"><span class="tagline">Boundless home loans</span></div>
    </section>
    <section class="contact-side">
      <svg class="pointer" width="30" height="34" viewBox="0 0 30 34"><polygon points="0,0 30,17 0,34" fill="#d8c8b8"/></svg>
      <div class="person-name">PETER WILKS</div>
      <div class="person-title">Co-Founder | Partner</div>
      <address class="address">14 Cassia Lane, Suite 310<br>Singapore 047219</address>
      <ul class="contact-list">
        <li class="contact-item">
          <svg class="contact-icon" viewBox="0 0 22 22"><path d="M3 8 Q11 2 19 8 L17 10 L14 8.5 L14 6.5 Q11 5.5 8 6.5 L8 8.5 L5 10 Z" fill="var(--icon-tone)"/><rect x="5" y="11" width="12" height="8" rx="1.5" fill="var(--icon-tone)"/><circle cx="11" cy="15" r="2" fill="var(--panel-red)"/></svg>
          <span>+65 555-0142</span>
        </li>
        <li class="contact-item">
          <svg class="contact-icon" viewBox="0 0 22 22"><rect x="2" y="6" width="18" height="11" fill="var(--icon-tone)"/><polyline points="2,6 11,13 20,6" fill="none" stroke="var(--panel-red)" stroke-width="1.5"/></svg>
          <span>peterwilks@hlc-example.asia</span>
        </li>
        <li class="contact-item">
          <svg class="contact-icon" viewBox="0 0 22 22"><circle cx="11" cy="11" r="8" fill="var(--icon-tone)"/><path d="M7 6 Q10 8 8 11 Q12 12 11 16 M13 5 Q15 8 17 9" fill="none" stroke="var(--panel-red)" stroke-width="1.6"/></svg>
          <span>www.hlc-example.asia</span>
        </li>
        <li class="contact-item">
          <svg class="contact-icon" viewBox="0 0 22 22"><circle cx="11" cy="11" r="8" fill="var(--icon-tone)"/></svg>
          <span>peterwilks</span>
        </li>
      </ul>
    </section>
  </div>
</body>
</html>
```